Anzeigengestaltung für Steuerberatungsgesellschaft
Zielgruppe
Die KTR Steuerberatungsgesellschaft mbH zählt zu einer der führenden Steuerberatungsgesellschaften für mittelständische Unternehmen in Sachsen. Unabhängig, professionell und vertrauensvoll. Getreu unserem Leitbild 'Unternehmer beraten Unternehmer' werden Sie von einem konstanten Beratungsteam betreut, welches sich an den Standorten Görlitz und Dres-den um ALLE Ihre steuerlichen Fragen und Themen kümmert. Darüber hinaus verfügen unse-re Mitarbeiter über ein umfangreiches betriebswirtschaftliches Fachwissen und sind daher jederzeit in der Lage, Sie auch in angrenzenden Themen zu unterstützen.
Aufgabenstellung
Siehe Briefing (ppt)

```html
<!DOCTYPE html>
<html lang="de">
<head>
<meta charset="utf-8">
<title>KTR Steuerberatung – Stellenanzeige</title>
<link href="https://fonts.googleapis.com/css2?family=Anton&family=Outfit:wght@400;600;700;800&display=swap" rel="stylesheet">
<style>
  :root {
    --stage: #b0b0b0;
    --red: #b8372f;
    --navy: #2d2c4c;
    --white: #ffffff;
    --text-dark: #2b2b33;
    --sky-top: #8fbde6;
    --sky-mid: #dbe9f5;
    --sky-low: #f4f7fa;
    --photo-light: #c9d6e4;
    --photo-mid: #7f93b3;
    --photo-deep: #34406f;
  }
  * { box-sizing: border-box; margin: 0; padding: 0; }
  html, body { width: 1200px; height: 1117px; overflow: hidden; background: var(--stage); }
  body { position: relative; font-family: "Outfit", sans-serif; }

  .ad {
    position: absolute; left: 79px; top: 282px; width: 1048px; height: 557px;
    overflow: hidden; background: var(--sky-low);
    box-shadow: 6px 8px 14px rgba(0,0,0,.25);
  }
  .ad__sky {
    position: absolute; inset: 0 0 154px 0;
    background: linear-gradient(180deg, var(--sky-top) 0%, var(--sky-mid) 45%, var(--sky-low) 100%);
  }
  .ad__photo {
    position: absolute; left: 590px; top: 140px; width: 458px; height: 330px;
    background: linear-gradient(180deg, var(--photo-light) 0%, var(--photo-mid) 45%, var(--photo-deep) 100%);
    border-radius: 40px 0 0 40px;
  }

  .ad__headline {
    position: absolute; left: 46px; top: 36px;
    font-family: "Anton", sans-serif; font-weight: 400;
    font-size: 66px; line-height: 72px; color: var(--red);
    -webkit-text-stroke: 10px var(--white); paint-order: stroke fill;
  }

  .ad__intro {
    position: absolute; left: 54px; top: 206px;
    font-size: 33px; font-weight: 700; color: var(--navy);
  }
  .ad__roles { position: absolute; left: 54px; top: 250px; list-style: none; }
  .ad__roles li {
    position: relative; padding-left: 37px;
    font-size: 27px; font-weight: 400; line-height: 36px; color: var(--text-dark);
  }
  .ad__roles li::before {
    content: ""; position: absolute; left: 0; top: 11px;
    border-left: 14px solid var(--red);
    border-top: 8px solid transparent; border-bottom: 8px solid transparent;
  }

  .ad__footer-band {
    position: absolute; left: 0; right: 0; top: 403px; bottom: 0; background: var(--navy);
  }
  .ad__bonus {
    position: absolute; left: 0; top: 342px; width: 644px; height: 126px;
    background: var(--red); border-radius: 0 64px 64px 0;
    display: flex; align-items: center; padding-left: 52px; color: var(--white);
  }
  .ad__bonus-amount { font-size: 100px; font-weight: 700; letter-spacing: -2px; line-height: 1; }
  .ad__bonus-label { font-size: 25px; font-weight: 600; margin-left: 10px; margin-top: 4px; }

  .ad__brand {
    position: absolute; left: 720px; top: 66px; width: 290px;
    font-size: 30px; font-weight: 700; color: var(--navy);
    text-align: right; white-space: nowrap;
  }
  .ad__partner-badge {
    position: absolute; left: 919px; top: 154px; width: 87px; height: 88px;
    background: var(--white);
  }

  .ad__contact {
    position: absolute; left: 54px; top: 478px; height: 34px;
    display: flex; align-items: center; color: var(--white); font-size: 20px;
  }
  .ad__locations { font-weight: 600; }
  .ad__divider { width: 2px; height: 34px; background: var(--white); margin: 0 16px; }
  .ad__hotline { font-weight: 400; }
  .ad__hotline strong { font-weight: 700; }

  .ad__apply {
    position: absolute; left: 737px; top: 476px; width: 257px; height: 50px;
    background: var(--red); border: 3px solid var(--white); border-radius: 25px;
    color: var(--white); font-size: 26px; font-weight: 700;
    display: flex; align-items: center; justify-content: center; padding-bottom: 4px;
  }
</style>
</head>
<body>
  <section class="ad">
    <div class="ad__sky" role="img" aria-label="Foto: heller Himmel mit Wolken"></div>
    <div class="ad__photo" role="img" aria-label="Foto: Mann im Anzug reitet auf einem Rollkoffer vor einer Großstadt-Skyline"></div>

    <h1 class="ad__headline">Auf der Suche nach<br>neuen Erfahrungen?</h1>

    <p class="ad__intro">Wir suchen dich!</p>
    <ul class="ad__roles">
      <li>Steuerfachangestellter (m/w/d)</li>
      <li>Steuerfachwirt (m/w/d)</li>
    </ul>

    <div class="ad__brand">KTR Steuerberatung</div>
    <div class="ad__partner-badge" aria-label="Partner-Siegel"></div>

    <div class="ad__footer-band"></div>
    <div class="ad__bonus">
      <span class="ad__bonus-amount">2.500€</span>
      <span class="ad__bonus-label">Wechselprämie</span>
    </div>

    <div class="ad__contact">
      <span class="ad__locations">Dresden/ Görlitz/ Home-Office</span>
      <span class="ad__divider"></span>
      <span class="ad__hotline">Jobhotline <strong>+49 3581 12 345 67</strong></span>
    </div>
    <div class="ad__apply">hier bewerben</div>
  </section>
</body>
</html>
```